hair salon business Card Design

My business name is Hair & Beauty @ Corrabin I want a Hot Pink and black business card with a loyalty program on the back after every 2nd haircut the third has $5 off and I will whole punch the squares My business phone number is (07) 54 913 668 address is Shop 2 3/9 Wollard st Corrabin Qld 4571 find us on facebook should be on the card somewhere with the facebook logo also a space alocated for your next appointment date n time also would like your har stylists name is Tess on the card somewhere easy to read you can check out my facebook site for images of my logo n shop signage

Industry/Entity Type

Hair

```html
<!DOCTYPE html>
<html lang="en">
<head>
<meta charset="utf-8">
<title>Hair &amp; Beauty @ Corrabin – Business Card</title>
<link rel="stylesheet" href="https://fonts.googleapis.com/css2?family=Delius&family=Oregano&display=swap">
<style>
  :root {
    --hot-pink: #ec0fc0;
    --hot-pink-deep: #c90aa3;
    --card-black: #232323;
    --text-light: #f4eef3;
    --stage: #e9e6e4;
  }
  html, body {
    margin: 0;
    padding: 0;
    width: 1200px;
    height: 936px;
    overflow: hidden;
    background: var(--stage);
  }
  .card {
    position: absolute;
    left: 100px;
    top: 182px;
    width: 1000px;
    height: 572px;
    background: var(--card-black);
    border-radius: 6px;
    overflow: hidden;
    font-family: "Delius", sans-serif;
    color: var(--text-light);
    box-shadow: 0 10px 30px rgba(0,0,0,.25);
  }
  .brand {
    position: absolute;
    left: 56px;
    top: 60px;
    display: flex;
    align-items: center;
    gap: 22px;
  }
  .brand-mark {
    width: 46px;
    height: 46px;
    background: var(--hot-pink);
  }
  .brand-name {
    margin: 0;
    font-size: 54px;
    font-weight: 400;
    color: var(--hot-pink);
    letter-spacing: .5px;
  }
  .contact-band {
    position: absolute;
    left: 0;
    top: 170px;
    width: 710px;
    height: 178px;
    background: var(--hot-pink);
  }
  .contact-row {
    position: absolute;
    display: flex;
    align-items: center;
    gap: 14px;
    font-size: 27px;
    color: var(--text-light);
  }
  .contact-row svg { width: 24px; height: 24px; flex: none; }
  .contact-address { left: 56px; top: 30px; }
  .contact-phone { left: 56px; top: 104px; }
  .contact-social { left: 390px; top: 104px; }
  .social-square {
    width: 20px;
    height: 20px;
    background: var(--text-light);
    flex: none;
  }
  .loyalty-ribbon {
    position: absolute;
    left: 150px;
    top: 390px;
    width: 520px;
    height: 120px;
  }
  .loyalty-ribbon svg { position: absolute; inset: 0; }
  .loyalty-text {
    position: absolute;
    inset: 0;
    display: flex;
    flex-direction: column;
    justify-content: center;
    align-items: center;
    font-family: "Oregano", cursive;
    font-size: 34px;
    line-height: 1.1;
    color: var(--text-light);
    text-align: center;
    padding-left: 40px;
  }
  .appointment-box {
    position: absolute;
    right: 34px;
    top: 150px;
    width: 230px;
    height: 300px;
    border: 4px solid var(--hot-pink);
    box-sizing: border-box;
    padding: 18px 16px;
    font-size: 22px;
    line-height: 1.25;
    color: var(--text-light);
  }
</style>
</head>
<body>
  <section class="card" aria-label="Hair &amp; Beauty @ Corrabin business card">
    <header class="brand">
      <span class="brand-mark"></span>
      <h1 class="brand-name">Hair &amp; Beauty @ Corrabin</h1>
    </header>

    <div class="contact-band">
      <div class="contact-row contact-address">
        <svg viewBox="0 0 24 24" aria-hidden="true"><path fill="#f4eef3" d="M12 2a7 7 0 0 0-7 7c0 5 7 13 7 13s7-8 7-13a7 7 0 0 0-7-7zm0 9.5a2.5 2.5 0 1 1 0-5 2.5 2.5 0 0 1 0 5z"/></svg>
        <span>Shop 2 3/9 Wollard st Corrabin Qld 4571</span>
      </div>
      <div class="contact-row contact-phone">
        <svg viewBox="0 0 24 24" aria-hidden="true"><path fill="#f4eef3" d="M6.6 10.8a15 15 0 0 0 6.6 6.6l2.2-2.2a1 1 0 0 1 1-.25 11.4 11.4 0 0 0 3.6.57 1 1 0 0 1 1 1V20a1 1 0 0 1-1 1A17 17 0 0 1 3 4a1 1 0 0 1 1-1h3.5a1 1 0 0 1 1 1c0 1.25.2 2.45.57 3.6a1 1 0 0 1-.25 1z"/></svg>
        <span>(07) 54 913 668</span>
      </div>
      <div class="contact-row contact-social">
        <span class="social-square"></span>
        <span>Hair-Beauty-at-Corrabin</span>
      </div>
    </div>

    <div class="loyalty-ribbon">
      <svg viewBox="0 0 520 120" preserveAspectRatio="none" aria-hidden="true">
        <polygon points="0,0 520,0 520,120 0,120 40,60" fill="#ec0fc0"/>
      </svg>
      <p class="loyalty-text" style="margin:0">After every 2nd haircut<br>the third has $5 off</p>
    </div>

    <div class="appointment-box">Next appointment Date &amp; Time</div>
  </section>
</body>
</html>
```